Brightmoor Card Company Business Cards

We are a trading card store with Zorblix, sports and other TCG cards, we need a business card design that encompasses a clean cut, modern style with a retro flare. website is brightmoorcardco.com for reference. Can utilize a comic book era feel or a more modern outdoor feel to utilize the "Pacific Northwest" elements of tress, mountains, etc.

Industry/Entity Type

Trading cards and collectibles

Contact Information for Business Card

business name, email address, phone number, name, owner job title

Font styles to use
Sans Serif

```html
<!DOCTYPE html>
<html lang="en">
<head>
<meta charset="UTF-8">
<title>Brightmoor Card Company – Business Cards</title>
<link href="https://fonts.googleapis.com/css2?family=Lato:wght@400&family=Montserrat:wght@700;800&display=swap" rel="stylesheet">
<style>
  :root {
    --backdrop: #3b3b3b;
    --brand-cyan: #10bee1;
    --card-light: #f6f6f6;
    --ink: #1e1e1e;
    --slate: #6f6f70;
    --white: #ffffff;
    --photo-top: #5a5d63;
    --photo-bottom: #2a2c33;
  }
  * { box-sizing: border-box; margin: 0; padding: 0; }
  html, body {
    width: 1200px; height: 1000px; overflow: hidden;
    background: var(--backdrop);
  }
  .canvas { position: relative; width: 1200px; height: 1000px; }

  .card {
    position: absolute; left: 194px; width: 812px; height: 463px;
    border-radius: 20px; overflow: hidden;
  }
  .card--front { top: 32px; background: var(--brand-cyan); }
  .card--back  { top: 505px; background: var(--card-light); }

  .brand-name {
    position: absolute; left: 0; right: 0; text-align: center;
    font-family: "Montserrat", sans-serif; font-weight: 800;
    text-transform: uppercase; line-height: 1.12;
  }
  .card--front .brand-name {
    top: 132px; color: var(--white); font-size: 50px; letter-spacing: 3px;
  }
  .card--back .brand-name {
    top: 120px; color: var(--slate); font-size: 26px; letter-spacing: 2px;
  }
  .brand-mark {
    display: block; margin: 0 auto; border-radius: 50%;
  }
  .card--front .brand-mark {
    width: 64px; height: 64px; background: var(--white); margin-bottom: 26px;
  }
  .card--back .brand-mark {
    width: 36px; height: 36px; background: var(--slate); margin-bottom: 14px;
  }

  .portrait {
    position: absolute; left: 655px; top: 26px; width: 130px; height: 156px;
    background: var(--white); border: 1px solid #dcdcdc; padding: 3px;
  }
  .portrait__fill {
    width: 100%; height: 100%;
    background: linear-gradient(180deg, var(--photo-top), var(--photo-bottom));
  }

  .role {
    position: absolute; right: 393px; top: 342px; text-align: right;
  }
  .role__store {
    font-family: "Montserrat", sans-serif; font-weight: 700;
    font-size: 31px; color: var(--brand-cyan); letter-spacing: 0.3px; line-height: 1.1;
  }
  .role__title {
    font-family: "Lato", sans-serif; font-size: 21px; color: var(--ink); margin-top: 3px;
  }
  .role__title span { color: var(--brand-cyan); }

  .contacts {
    position: absolute; left: 466px; top: 329px; list-style: none;
    font-family: "Lato", sans-serif; font-size: 22px; color: var(--ink);
  }
  .contacts li { display: flex; align-items: center; height: 26px; margin-bottom: 10px; }
  .contacts svg { width: 27px; height: 27px; margin-right: 11px; flex: none; }
</style>
</head>
<body>
<div class="canvas">

  <section class="card card--front">
    <div class="brand-name"><span class="brand-mark"></span>Brightmoor<br>Card Company</div>
  </section>

  <section class="card card--back">
    <div class="portrait"><div class="portrait__fill" role="img" aria-label="Portrait photo of the store manager"></div></div>

    <div class="brand-name"><span class="brand-mark"></span>Brightmoor<br>Card Company</div>

    <div class="role">
      <div class="role__store">TRADING CARD STORE</div>
      <div class="role__title">Store <span>Manager</span></div>
    </div>

    <ul class="contacts">
      <li>
        <svg viewBox="0 0 28 28" fill="none" stroke="#10bee1" stroke-width="1.8">
          <rect x="1.5" y="1.5" width="25" height="25" rx="4"/>
          <path d="M9 7.5l2.5-.5 1.6 3.6-1.7 1.2c.8 1.8 2 3 3.8 3.8l1.2-1.7 3.6 1.6-.5 2.5c-5.8.4-10.9-4.7-10.5-10.5z" stroke-linejoin="round"/>
        </svg>
        044-555 218 406
      </li>
      <li>
        <svg viewBox="0 0 28 28" fill="none" stroke="#10bee1" stroke-width="1.8" stroke-linejoin="round">
          <rect x="1.5" y="1.5" width="25" height="25" rx="4"/>
          <path d="M7 13.5l14-6-4 14-3.5-5z M13.5 16.5L21 7.5"/>
        </svg>
        info@brightmoormail.com
      </li>
      <li>
        <svg viewBox="0 0 28 28" fill="none" stroke="#10bee1" stroke-width="1.8">
          <rect x="1.5" y="1.5" width="25" height="25" rx="4"/>
          <circle cx="14" cy="14" r="7"/>
          <ellipse cx="14" cy="14" rx="3" ry="7"/>
          <path d="M7 14h14"/>
        </svg>
        www.brightmoorcardco.com
      </li>
    </ul>
  </section>

</div>
</body>
</html>
```